Call to action - Postcard Design

Design a post card keeping in mind the following;

1. double sided
2. 4" x6" (10.16cm x 15.24cm)
3. call to action message "Fast Free Quote" using a similar feel to our trade show booth design and brochure.
5. need to include the four vertical market logos "cameras, access, alarm, intercom"
6. an image and brief description on the back of the postcard with the call to action;
a. Camera Systems "easy to use software, remote monitoring from any device, motion activated"
b. Access Control "web browser credential management and allow/deny access from anywhere"
7. review our slides on the front page of our website http://www.keplowmart.com

Target Market(s)

B2B - business owners, managers, purchasers

Industry/Entity Type

Call

Requirements
Must have
• - call to action to get clients to contact us for a free quote
• - use a similar design to our trade show booth
• - clean look (uncluttered)

```html
<!DOCTYPE html>
<html lang="en">
<head>
<meta charset="utf-8">
<title>Keplow Mart – Free Quote Postcard</title>
<link href="https://fonts.googleapis.com/css2?family=Montserrat:wght@300;400;800&family=Oswald:wght@400;500&display=swap" rel="stylesheet">
<style>
  :root{
    --navy:#0f2a57;
    --navy-deep:#0a2149;
    --orange:#f04e23;
    --white:#ffffff;
    --backdrop:#5e5e5e;
    --line:#5a6e9a;
  }
  *{box-sizing:border-box;margin:0;padding:0}
  html,body{width:1200px;height:1200px;overflow:hidden}
  body{background:var(--backdrop);position:relative;font-family:"Oswald",sans-serif}
  .postcard{position:absolute;left:180px;width:840px;height:560px;overflow:hidden;background:var(--navy);box-shadow:0 6px 18px rgba(0,0,0,.35)}
  .postcard--front{top:20px}
  .postcard--back{top:620px;background:var(--white)}
  .shape-layer{position:absolute;inset:0}

  /* brand name */
  .brand{position:absolute;display:flex;align-items:center;gap:10px;color:var(--white);font-family:"Oswald",sans-serif;font-weight:500;text-transform:uppercase;letter-spacing:1px}
  .brand__mark{width:22px;height:22px;background:var(--white)}
  .front__brand{left:46px;top:46px;font-size:30px}
  .back__brand{left:110px;top:330px;font-size:40px}
  .back__brand .brand__mark{width:30px;height:30px}

  /* front */
  .people-row{position:absolute;left:46px;top:120px;width:430px;height:120px;background:linear-gradient(90deg,var(--white) 0 76%,var(--orange) 76% 86%,var(--white) 86%);opacity:.92;border-radius:4px}
  .story{position:absolute;left:46px;top:270px;width:470px;color:var(--white);font-size:21px;line-height:1.3;text-transform:uppercase;letter-spacing:.3px}
  .story__lead{color:var(--orange)}
  .markets{position:absolute;left:46px;top:410px;display:flex;gap:26px}
  .market{display:flex;flex-direction:column;align-items:center;gap:6px;color:var(--white);font-size:14px}
  .market svg{width:64px;height:64px}
  .device-screens{position:absolute;left:560px;top:60px;width:260px;height:300px;background:linear-gradient(160deg,#2b2b2b,#5d6a78 55%,#1c1c1c);border-radius:10px}

  /* back */
  .cta{position:absolute;left:50px;top:70px;color:var(--white)}
  .cta__title{font-family:"Montserrat",sans-serif;font-weight:800;font-size:34px;color:var(--orange);text-transform:uppercase;letter-spacing:1px;white-space:nowrap}
  .cta__sub{font-family:"Montserrat",sans-serif;font-weight:300;font-size:31px;text-transform:uppercase;margin-top:4px;white-space:nowrap}
  .dome-camera{position:absolute;left:120px;top:200px;width:280px;height:280px;border-radius:50%;background:radial-gradient(circle at 50% 65%,rgba(240,78,35,.55),rgba(15,42,87,.2) 60%,transparent 72%)}
  .contact{position:absolute;left:60px;top:460px;color:var(--white);font-family:"Montserrat",sans-serif;font-size:15px;letter-spacing:6px;text-transform:uppercase;line-height:1.75}
  .stamp-box{position:absolute;right:40px;top:60px;width:84px;height:96px;border:1px solid var(--line)}
  .address-lines{position:absolute;left:622px;top:210px;width:180px}
  .address-lines span{display:block;height:44px;border-bottom:1px solid var(--line)}
</style>
</head>
<body>

<section class="postcard postcard--front" aria-label="Postcard front">
  <svg class="shape-layer" viewBox="0 0 840 560" aria-hidden="true">
    <path d="M600 0 L840 0 L840 400 L620 410 C560 300 560 120 600 0Z" fill="var(--white)"/>
    <path d="M582 0 L600 0 C560 120 560 300 620 410 L840 400 L840 412 L612 424 C546 300 546 120 582 0Z" fill="var(--orange)"/>
    <path d="M640 470 L840 440 L840 500 L690 505Z" fill="var(--orange)"/>
    <rect x="0" y="548" width="840" height="12" fill="var(--orange)"/>
  </svg>

  <div class="brand front__brand"><span class="brand__mark"></span>Keplow Mart</div>
  <div class="people-row" role="img" aria-label="Row of employee pictograms, one highlighted in orange"></div>

  <p class="story"><span class="story__lead">From its humble beginning in 1999,</span> Keplow Mart employees have worked hard to become one of Canada's most trusted commercial security integrators.</p>

  <div class="markets">
    <div class="market">
      <svg viewBox="0 0 64 64" aria-hidden="true"><circle cx="32" cy="32" r="29" fill="none" stroke="#fff" stroke-width="3"/><rect x="18" y="26" width="24" height="12" fill="#fff" transform="rotate(-20 30 32)"/><rect x="26" y="38" width="4" height="10" fill="#fff"/></svg>
      <span>Cameras</span>
    </div>
    <div class="market">
      <svg viewBox="0 0 64 64" aria-hidden="true"><circle cx="32" cy="32" r="29" fill="none" stroke="#fff" stroke-width="3"/><circle cx="38" cy="24" r="7" fill="none" stroke="#fff" stroke-width="3"/><path d="M33 29 L20 44 M24 40 L28 44" stroke="#fff" stroke-width="3"/><path d="M12 12 L52 52" stroke="#fff" stroke-width="3"/></svg>
      <span>Access</span>
    </div>
    <div class="market">
      <svg viewBox="0 0 64 64" aria-hidden="true"><circle cx="32" cy="32" r="29" fill="none" stroke="#fff" stroke-width="3"/><rect x="21" y="16" width="22" height="32" rx="3" fill="none" stroke="#fff" stroke-width="3"/><rect x="25" y="20" width="14" height="7" fill="#fff"/><g fill="#fff"><rect x="25" y="31" width="4" height="4"/><rect x="30" y="31" width="4" height="4"/><rect x="35" y="31" width="4" height="4"/><rect x="25" y="38" width="4" height="4"/><rect x="30" y="38" width="4" height="4"/><rect x="35" y="38" width="4" height="4"/></g></svg>
      <span>Alarm</span>
    </div>
    <div class="market">
      <svg viewBox="0 0 64 64" aria-hidden="true"><circle cx="32" cy="32" r="29" fill="none" stroke="#fff" stroke-width="3"/><path d="M20 18v12M26 16v14M32 16v14M38 16v14M44 18v12" stroke="#fff" stroke-width="3"/><path d="M18 36 Q32 48 46 36" fill="none" stroke="#fff" stroke-width="3"/></svg>
      <span>Intercom</span>
    </div>
  </div>

  <div class="device-screens" role="img" aria-label="Tablet and smartphone showing live camera monitoring views"></div>
</section>

<section class="postcard postcard--back" aria-label="Postcard back">
  <svg class="shape-layer" viewBox="0 0 840 560" aria-hidden="true">
    <path d="M0 0 L580 0 C552 140 552 300 580 430 L0 430Z" fill="var(--navy)"/>
    <path d="M580 0 L600 0 C572 140 572 300 600 430 L580 430 C552 300 552 140 580 0Z" fill="var(--orange)"/>
    <path d="M0 430 L600 430 C700 430 780 400 840 370 L840 560 L0 560Z" fill="var(--orange)"/>
    <path d="M770 0 L840 0 L840 60 C815 35 795 15 770 0Z" fill="var(--orange)"/>
  </svg>

  <div class="dome-camera" role="img" aria-label="Dome security camera, faded into the background"></div>

  <div class="cta">
    <p class="cta__title">Visit our website</p>
    <p class="cta__sub">For your free quote!</p>
  </div>

  <div class="brand back__brand"><span class="brand__mark"></span>Keplow Mart</div>

  <p class="contact">Toll free: 877.555.0142<br>sales@keplowmart.com<br>www.keplowmart.com</p>

  <div class="stamp-box"></div>
  <div class="address-lines"><span></span><span></span><span></span><span></span></div>
</section>

</body>
</html>
```